Stylish Business Card for Modern hair salon

I need a simple business card design using our salon logo and colours that are in the logo. We service clients of all ages but predominantly those in the 18 to 55 age range. We have a young staff and are looking to have a card that will present a modern and clean image that represents who we are. The card should be in black and white same as our logo. Minimal use of other colours is allowed.

Industry/Entity Type

Hair And Beauty

Contact Information for Business Card

The design should have the following information
salon name - TR Hair Studio
address - 2751 Birchfield Rd.E. Mississauga, ON L7P3K2
phone - 905 614-2870
website - trhairexample.ca
instagram - tr.hairstudio
twitter - @TR_HairStudio

Colors
000000
ffffff
474747

Requirements
Must have
• simple design, salon name, address, phone, website, instagram, twitter info
• Back of card should have the following:
• YOUR NEXT APPOINTMENT
• DATE
• TIME
Nice to have
• simple design, clear to see and read,
• predominantly black and white colour, minimal use of other colours is ok
Should not have
• many colours, various fonts

```html
<!DOCTYPE html>
<html lang="en">
<head>
<meta charset="utf-8">
<title>TR Hair Studio – Business Card</title>
<link href="https://fonts.googleapis.com/css2?family=Open+Sans:wght@400;600;700&display=swap" rel="stylesheet">
<style>
  :root {
    --stage: #2f2b29;
    --card: #0d0d0d;
    --white: #ffffff;
    --grey: #474747;
    --silver: #b9b9b9;
    --soft: #d6d6d6;
  }
  * { margin: 0; padding: 0; box-sizing: border-box; }
  html, body {
    width: 1200px; height: 864px; overflow: hidden;
    background: var(--stage);
    font-family: "Open Sans", sans-serif;
  }
  .stage {
    width: 1200px; height: 864px;
    display: flex; align-items: center; justify-content: center; gap: 40px;
  }
  .card {
    width: 540px; height: 309px;
    background: var(--card);
    border-radius: 4px;
    position: relative;
    display: flex; align-items: center;
    box-shadow: 0 10px 30px rgba(0,0,0,.45);
  }
  .brand {
    display: flex; flex-direction: column; align-items: center;
    width: 210px; padding-left: 28px;
  }
  .brand-name {
    font-weight: 600; color: var(--white);
    font-size: 30px; line-height: 1.15; text-align: center; letter-spacing: 1px;
  }
  .back .brand-name { color: var(--silver); }
  .brand-rule {
    margin-top: 10px; width: 150px; height: 1px; background: var(--silver);
  }
  .divider {
    width: 1px; height: 150px; margin: 0 26px 0 30px;
    background: linear-gradient(to bottom, transparent, var(--grey) 20%, var(--silver) 50%, var(--grey) 80%, transparent);
  }
  .contact { color: var(--soft); font-size: 14px; line-height: 1.45; }
  .contact .person { font-weight: 700; color: var(--silver); font-size: 13px; letter-spacing: .5px; }
  .contact .role { color: var(--white); font-size: 15px; margin-bottom: 2px; }
  .contact ul { list-style: none; }
  .contact li { display: flex; align-items: center; gap: 8px; color: var(--white); }
  .contact svg { width: 12px; height: 12px; flex: none; }
  .appointment { color: var(--silver); padding-left: 30px; width: 280px; }
  .appointment h2 { font-size: 17px; font-weight: 700; margin-bottom: 14px; }
  .field { display: flex; align-items: flex-end; font-size: 14px; margin-bottom: 14px; }
  .field .fill { flex: 1; border-bottom: 1px dotted var(--silver); margin-left: 4px; height: 14px; }
  .field .suffix { font-size: 10px; margin-left: 4px; }
</style>
</head>
<body>
<main class="stage">

  <section class="card back" aria-label="Card back">
    <div class="brand">
      <span class="brand-name">TR Hair<br>Studio</span>
      <span class="brand-rule"></span>
    </div>
    <div class="appointment">
      <h2>Your Next Appointment</h2>
      <div class="field">Date:<span class="fill"></span></div>
      <div class="field">Time:<span class="fill"></span><span class="suffix">AM/PM</span></div>
    </div>
  </section>

  <section class="card front" aria-label="Card front">
    <div class="brand">
      <span class="brand-name">TR Hair<br>Studio</span>
      <span class="brand-rule"></span>
    </div>
    <span class="divider"></span>
    <div class="contact">
      <div class="person">ALEX MORENO</div>
      <div class="role">CEO/FOUNDER</div>
      <div>2751 Birchfield Rd.E.</div>
      <div>Mississauga, ON L7P3K2</div>
      <ul>
        <li><svg viewBox="0 0 12 12"><path fill="#fff" d="M2.5 1h2l1 2.5-1.2.9a6 6 0 0 0 3.3 3.3l.9-1.2 2.5 1v2c0 .8-.7 1.5-1.5 1.5A9 9 0 0 1 1 2.5C1 1.7 1.7 1 2.5 1z"/></svg>905 614-2870</li>
        <li><svg viewBox="0 0 12 12"><circle cx="6" cy="6" r="5" fill="none" stroke="#fff" stroke-width="1.2"/><path d="M1 6h10M6 1c2 2 2 8 0 10M6 1c-2 2-2 8 0 10" fill="none" stroke="#fff" stroke-width=".9"/></svg>www.trhairexample.ca</li>
        <li><svg viewBox="0 0 12 12"><circle cx="6" cy="6" r="5" fill="#fff"/></svg>@TR_HairStudio</li>
        <li><svg viewBox="0 0 12 12"><rect x="1" y="1" width="10" height="10" rx="2" fill="#fff"/></svg>tr.hairstudio</li>
      </ul>
    </div>
  </section>

</main>
</body>
</html>
```